Poster Design Project for Over 50's Gym

We need a poster design to advertise our over 50's gym. We want to attract older adults who love enjoying their age, living life and having a bit of fun.
We would like to see a bright, fun, non-intimidating poster communicating how easy exercise can be and how great it can be for your health.
I would like the poster to include the following information.
Title:
Tullarow's Over 50's Gym
Exercise with confidence
How old would you be if you didn't know your age?
Suitable exercise programmes for all medical conditions
Friendly and non-intimidating environment
Private health insurance rebates
University qualified exercise physiologists
Vital Steps Exercise Physiology Clinic
Exercise Physiologists Danielle Prewitt & Tobias Lindqvist
Suite 7, 245 Corrigan Road, Mackay
www.tullarowvital.com.au
MON - FRI 8:30 am - 6:30 pm
I have photos available for use & Logo just unable to attach at moment****

```html
<!DOCTYPE html>
<html lang="en">
<head>
<meta charset="utf-8">
<title>Tullarow's Over 50's Gym – Poster</title>
<link href="https://fonts.googleapis.com/css2?family=Oswald:wght@500&family=Roboto+Condensed:wght@400;500&display=swap" rel="stylesheet">
<style>
  :root {
    --orange: #f26a1b;
    --orange-light: #f9a13c;
    --orange-deep: #e2500f;
    --charcoal: #3a3a3c;
    --ink: #2b2b2b;
    --red: #d4252a;
    --paper: #ffffff;
    --mist: #e9eaec;
  }
  * { margin: 0; padding: 0; box-sizing: border-box; }
  html, body { width: 914px; height: 1200px; overflow: hidden; background: var(--paper); }
  .poster {
    position: relative;
    width: 914px;
    height: 1200px;
    overflow: hidden;
    background: radial-gradient(ellipse at 55% 35%, #ffffff 0%, var(--mist) 75%);
    font-family: "Roboto Condensed", "Arial Narrow", sans-serif;
    color: var(--ink);
  }
  .hero-art { position: absolute; inset: 0; width: 914px; height: 1200px; }
  .web-address {
    position: absolute;
    left: 30px; top: 14px;
    font-size: 15px;
    font-weight: 500;
    color: var(--charcoal);
  }
  .brand {
    position: absolute;
    left: 115px; top: 905px;
    width: 265px;
    display: flex;
    align-items: flex-start;
    gap: 12px;
  }
  .brand-mark {
    flex: none;
    width: 22px; height: 22px;
    margin-top: 10px;
    background: var(--orange);
  }
  .brand-name {
    font-family: "Oswald", "Arial Narrow", sans-serif;
    font-weight: 500;
    font-size: 44px;
    line-height: 1.05;
    text-transform: uppercase;
    color: var(--charcoal);
  }
  .details {
    position: absolute;
    left: 403px; top: 896px;
    list-style: none;
    font-size: 16.5px;
    line-height: 24px;
    color: var(--ink);
  }
  .details .clinic { margin-top: 10px; }
  .footer {
    position: absolute;
    left: 70px; right: 70px; top: 1125px;
    border-top: 1px solid #c9c9c9;
    padding-top: 12px;
    text-align: center;
    font-size: 14.5px;
    color: var(--charcoal);
    white-space: nowrap;
  }
  .footer .dot { color: var(--orange); margin: 0 4px; }
  .footer .phone { color: var(--red); }
</style>
</head>
<body>
<main class="poster">
  <svg class="hero-art" viewBox="0 0 914 1200" aria-hidden="false">
    <defs>
      <linearGradient id="people-tones" x1="0" y1="0" x2="1" y2="1">
        <stop offset="0" stop-color="#e8b48f"/>
        <stop offset="0.35" stop-color="#6b3fa0"/>
        <stop offset="0.7" stop-color="#9cc52a"/>
        <stop offset="1" stop-color="#c9d88e"/>
      </linearGradient>
      <linearGradient id="swoosh-fill" x1="0" y1="0" x2="1" y2="0">
        <stop offset="0" stop-color="var(--orange-deep)"/>
        <stop offset="0.5" stop-color="var(--orange)"/>
        <stop offset="1" stop-color="var(--orange-light)"/>
      </linearGradient>
    </defs>

    <rect class="hero-photo" role="img" aria-label="Photo of two smiling women, one older with white hair in a green top and one younger in purple, each lifting an orange dumbbell"
          x="190" y="150" width="560" height="640" rx="60" fill="url(#people-tones)" opacity="0.55"/>

    <path class="lower-panel" d="M0,640 C260,830 560,800 914,600 L914,1200 L0,1200 Z" fill="#f7f7f8"/>

    <path class="swoosh-glow" d="M0,330 C190,540 520,690 914,510 L914,545 C520,720 200,580 0,380 Z" fill="var(--orange-light)" opacity="0.55"/>
    <path class="swoosh-band" d="M0,360 C180,560 520,700 914,540 L914,600 C560,790 260,830 0,640 Z" fill="url(#swoosh-fill)"/>
    <path class="swoosh-line" d="M0,470 C220,680 540,740 914,570" fill="none" stroke="#ffffff" stroke-width="2" opacity="0.45"/>
    <path class="swoosh-line" d="M0,560 C240,760 560,770 914,585" fill="none" stroke="#ffd3a8" stroke-width="3" opacity="0.6"/>
  </svg>

  <p class="web-address">www.tullarowvital.com.au</p>

  <div class="brand">
    <span class="brand-mark"></span>
    <span class="brand-name">Tullarow's Over 50's Gym</span>
  </div>

  <ul class="details">
    <li>Exercise with confidence</li>
    <li>How old would you be if you didn't know your age?</li>
    <li>Suitable exercise programmes for all medical conditions</li>
    <li>Friendly and non-intimidating environment</li>
    <li>Private health insurance rebates</li>
    <li>University qualified exercise physiologists</li>
    <li class="clinic">Vital Steps Exercise Physiology Clinic</li>
    <li>Exercise Physiologists Danielle Prewitt &amp; Tobias Lindqvist</li>
  </ul>

  <p class="footer">
    Suite 7, 245 Corrigan Road, Mackay, MON - FRI 8:30 am - 6:30 pm
    <span class="dot">•</span><span class="phone">T (07) 4000 1234</span>
    <span class="dot">•</span><span class="phone">F (07) 4000 5678</span>
    <span class="dot">•</span>admin@tullarowvital.com.au
  </p>
</main>
</body>
</html>
```